Business cards — need something that creates “wow” factor

Need a sleek and clean looking business card. Something that is clear and consise. These business cards are for my painting business and hundreds will be placed in the Dallas area between all Halverd Pemberton paint stored. These card really need to stick out! Open to any and all ideas...

Target Market(s)

Residential clientele

Industry/Entity Type

Painting

Contact Information for Business Card

Dorian Vakelby
Owner

382.516.2074

Web: Mesahuepainting.example (still under construction)
Mesahuepainting@mailbox.example

Font styles to use
Sans Serif

Colors

Designer to choose colors to be used in the design.

Requirements
Must have
• My name, number, website, email, Socialpage
• and “100% customer satisfaction guaranteed”
• Socialpage.example/Mesahuepainting/
Nice to have
• Listed services
• Interior/exterior painting
• Drywall repair/texture
• Fence staining/refinishing
• Concrete staining
• Epoxy flooring
• Pressure washing

```html
<!DOCTYPE html>
<html lang="en">
<head>
<meta charset="utf-8">
<title>Mesa Hue – Business Card</title>
<link href="https://fonts.googleapis.com/css2?family=Raleway:wght@400;500;700&display=swap" rel="stylesheet">
<style>
  :root {
    --page-bg: #e9eaec;
    --card-white: #ffffff;
    --teal-light: #07b39b;
    --teal-dark: #06626f;
    --band-black: #050505;
    --ink: #1b1b1b;
    --ink-soft: #6b6b6b;
    --white: #ffffff;
  }
  * { box-sizing: border-box; margin: 0; padding: 0; }
  html, body {
    width: 1200px; height: 950px; overflow: hidden;
    background: var(--page-bg);
    font-family: "Raleway", sans-serif;
  }
  .card {
    position: absolute; left: 240px;
    width: 720px; height: 411px;
    box-shadow: 0 8px 24px rgba(0,0,0,.18);
    overflow: hidden;
  }
  /* Front */
  .card-front { top: 45px; background: var(--card-white); }
  .brand {
    position: absolute; left: 0; right: 0; top: 140px;
    text-align: center;
  }
  .brand-name {
    font-size: 76px; font-weight: 700; letter-spacing: 2px;
    color: var(--ink); text-transform: uppercase; line-height: 1;
  }
  .brand-tagline {
    margin-top: 18px; font-size: 15px; color: var(--ink-soft); letter-spacing: .5px;
  }
  /* Back */
  .card-back { top: 494px; background: var(--band-black); }
  .back-shape { position: absolute; inset: 0; }
  .person { position: absolute; left: 52px; top: 38px; color: var(--white); }
  .person-name { font-size: 38px; font-weight: 400; line-height: 1; }
  .person-name strong { font-weight: 700; }
  .person-role { font-size: 20px; margin-top: 4px; }
  .phone {
    position: absolute; left: 52px; top: 128px;
    display: flex; align-items: center; gap: 22px; color: var(--white);
  }
  .phone-number { font-size: 40px; font-weight: 500; letter-spacing: 1px; }
  .divider {
    position: absolute; left: 52px; top: 198px; width: 340px;
    border-top: 2px solid var(--white);
  }
  .contacts {
    position: absolute; left: 52px; top: 216px; list-style: none; color: var(--white);
    font-size: 19px;
  }
  .contacts li { display: flex; align-items: center; gap: 12px; height: 34px; }
  .contacts svg { flex: none; }
  .services {
    position: absolute; left: 470px; top: 130px; color: var(--white);
    font-size: 18px; list-style: none;
  }
  .services li { position: relative; padding-left: 18px; height: 31px; }
  .services li::before {
    content: ""; position: absolute; left: 0; top: 8px;
    width: 6px; height: 6px; border-radius: 50%; background: var(--white);
  }
  .guarantee {
    position: absolute; left: 300px; bottom: 12px;
    color: var(--white); font-size: 17px; font-weight: 500;
  }
</style>
</head>
<body>
  <section class="card card-front">
    <div class="brand">
      <div class="brand-name">Mesa Hue</div>
      <div class="brand-tagline">Commercial | Residential | Interior | Exterior</div>
    </div>
  </section>

  <section class="card card-back">
    <svg class="back-shape" width="720" height="411" viewBox="0 0 720 411">
      <defs>
        <linearGradient id="tealGrad" x1="0" y1="0" x2="1" y2="1">
          <stop offset="0" stop-color="var(--teal-light)"/>
          <stop offset="1" stop-color="var(--teal-dark)"/>
        </linearGradient>
      </defs>
      <path d="M0 0 H720 V365 H300 Q270 365 262 380 L248 411 H0 Z" fill="url(#tealGrad)"/>
    </svg>

    <div class="person">
      <div class="person-name"><strong>Dorian</strong> Vakelby</div>
      <div class="person-role">Owner</div>
    </div>

    <div class="phone">
      <svg width="48" height="48" viewBox="0 0 48 48" aria-hidden="true">
        <circle cx="24" cy="24" r="21" fill="none" stroke="#fff" stroke-width="3"/>
        <path d="M19 13 c-4 2 -5 6 -3 11 c2 5 5 9 10 11 c3 1 5 0 6 -2 l-4 -5 l-3 2 c-2 -1 -4 -4 -5 -7 l3 -2 z" fill="#fff"/>
      </svg>
      <span class="phone-number">382.516.2074</span>
    </div>

    <div class="divider"></div>

    <ul class="contacts">
      <li>
        <svg width="24" height="18" viewBox="0 0 24 18" aria-hidden="true"><rect x="1" y="1" width="22" height="16" fill="#fff"/><path d="M1 1 L12 10 L23 1" fill="none" stroke="#08807f" stroke-width="2"/></svg>
        Mesahuepainting@mailbox.example
      </li>
      <li>
        <svg width="24" height="24" viewBox="0 0 24 24" aria-hidden="true"><g fill="none" stroke="#fff" stroke-width="2"><circle cx="12" cy="12" r="10"/><ellipse cx="12" cy="12" rx="4.5" ry="10"/><path d="M2 12 H22 M4 7 H20 M4 17 H20"/></g></svg>
        www.Mesahuepainting.example
      </li>
      <li>
        <svg width="24" height="24" viewBox="0 0 24 24" aria-hidden="true"><circle cx="12" cy="12" r="11" fill="#fff"/></svg>
        Socialpage.example/Mesahuepainting/
      </li>
    </ul>

    <ul class="services">
      <li>Interior/exterior painting</li>
      <li>Drywall repair/texture</li>
      <li>Fence staining/refinishing</li>
      <li>Concrete staining</li>
      <li>Epoxy flooring</li>
      <li>Pressure washing</li>
    </ul>

    <div class="guarantee">100% customer satisfaction guaranteed</div>
  </section>
</body>
</html>
```